Financial Planner Marketing Post Card

I'm a Financial Planner and Managing Principal of our Washington DC office (we're a boutique firm based out of California).The name of my firm is The Wexmoor Group, LLC. We specialize in investment strategies and Estate Planning. We offer everything from Estate Planning to Education Planning to Risk Management along with Insurance Planning. But I want my post card to really highlight is the main product I'm trying to sell with are the Fiduciary Standards of Being a RAS (Registered Asset Steward). I will attach a file with the Fiduciary Standards, along with a list of my service and products, company logo, along with a personal slogan. I would like for there to be room on my post card for my photo as well. I would like to use both sides of the post card with color; along with room for the ADPS postage.

Boutique

```html
<!DOCTYPE html>
<html lang="en">
<head>
<meta charset="utf-8">
<title>The Wexmoor Group, LLC – Postcard</title>
<link href="https://fonts.googleapis.com/css2?family=Montserrat:wght@600;700&family=Tinos:ital,wght@0,400;0,700;1,400&display=swap" rel="stylesheet">
<style>
  :root{
    --navy:#0b1a6e;
    --royal:#1450a8;
    --ocean:#1f78c4;
    --cyan:#19b6e6;
    --sky:#dcebfb;
    --ink:#1a1a1a;
    --white:#ffffff;
    --stage:#eef1f5;
  }
  *{box-sizing:border-box;margin:0;padding:0}
  html,body{width:1200px;height:900px;overflow:hidden;background:var(--stage)}
  .canvas{position:relative;width:1200px;height:900px;display:flex;gap:32px;align-items:center;justify-content:center}
  .postcard{position:relative;width:560px;height:400px;background:var(--white);overflow:hidden;box-shadow:0 6px 20px rgba(0,0,0,.18)}
  .postcard svg.shapes{position:absolute;inset:0}

  /* front */
  .credentials{position:absolute;left:20px;top:26px;width:255px;font-family:"Montserrat",sans-serif;font-weight:700;font-size:18px;line-height:1.2;color:var(--white)}
  .brand{position:absolute;right:26px;top:32px;display:flex;align-items:center;gap:8px;font-family:"Tinos",serif;font-weight:700;font-size:15px;color:var(--navy)}
  .brand .mark{width:16px;height:16px;background:var(--ocean)}
  .services-visual{position:absolute;left:282px;top:150px;width:110px;height:110px;border-radius:50%;background:radial-gradient(circle,#ffffff 0%,#e4eefa 55%,rgba(200,220,244,0) 100%)}
  .portrait{position:absolute;right:0;top:112px;width:170px;height:188px;background:linear-gradient(180deg,#c9d3df 0%,#2b3550 100%)}
  .cta-band{position:absolute;left:0;top:300px;width:100%;height:30px;background:linear-gradient(90deg,var(--royal),var(--cyan));color:var(--white);font-family:"Montserrat",sans-serif;font-weight:600;font-size:14px;line-height:30px;padding-left:20px}
  .name-band{position:absolute;left:0;top:330px;width:100%;height:70px;background:var(--navy);color:var(--white);padding:6px 20px}
  .name-band .advisor{font-family:"Tinos",serif;font-weight:700;font-size:29px;line-height:1.1}
  .name-band .role{font-family:"Tinos",serif;font-size:13px;margin-top:2px}

  /* back */
  .fiduciary{position:absolute;left:18px;top:20px;width:270px;border:1px solid rgba(255,255,255,.8);padding:8px 10px;font-family:"Tinos",serif;font-size:10.5px;line-height:1.35;color:var(--white)}
  .fiduciary h3{font-size:12px;margin-bottom:3px}
  .fiduciary li{margin-left:12px}
  .slogan{position:absolute;left:22px;top:200px;width:190px;font-family:"Tinos",serif;font-weight:700;font-style:italic;font-size:15px;line-height:1.2;color:var(--white)}
  .height-list{position:absolute;left:130px;top:272px;list-style:none;font-family:"Tinos",serif;font-size:11.5px;line-height:1.35;color:var(--white);border-left:1px solid rgba(255,255,255,.8);padding-left:8px}
  .return-address{position:absolute;left:326px;top:34px;width:140px;font-family:"Tinos",serif;font-style:normal;font-size:8.5px;line-height:1.4;color:var(--ink)}
  .return-address .brand-name{display:flex;align-items:center;gap:5px;font-weight:700;font-size:10px;color:var(--navy);margin-bottom:3px;white-space:nowrap}
  .return-address .brand-name i{width:9px;height:9px;background:var(--ocean);display:inline-block}
  .stamp-box{position:absolute;right:22px;top:34px;width:64px;height:74px;border:3px solid var(--ink)}
  .address-lines{position:absolute;left:352px;top:200px;width:186px}
  .address-lines span{display:block;height:34px;border-bottom:2px dotted #555}
</style>
</head>
<body>
<main class="canvas">

  <section class="postcard front">
    <svg class="shapes" width="560" height="400" viewBox="0 0 560 400">
      <defs>
        <linearGradient id="skyFade" x1="0" y1="0" x2="1" y2="1">
          <stop offset="0" stop-color="#ffffff"/><stop offset="1" stop-color="#cfe2f8"/>
        </linearGradient>
        <linearGradient id="deskPhoto" x1="0" y1="0" x2="1" y2="1">
          <stop offset="0" stop-color="#2f8fd6"/><stop offset=".6" stop-color="#155ea8"/><stop offset="1" stop-color="#0d3f86"/>
        </linearGradient>
      </defs>
      <rect width="560" height="300" fill="url(#skyFade)"/>
      <path d="M0 0 H300 Q250 150 300 300 H0 Z" fill="url(#deskPhoto)" role="img" aria-label="Blue-toned photo of a hand writing financial plans at a desk"/>
    </svg>
    <p class="credentials">Registered Asset Steward, Certified Portfolio Strategy Analyst, Certified Wealth and Trust Advisor.</p>
    <div class="brand"><span class="mark"></span>The Wexmoor Group, LLC</div>
    <div class="services-visual" role="img" aria-label="Illustration of the firm's service areas"></div>
    <div class="portrait" role="img" aria-label="Portrait photo of the advisor in a dark suit, arms crossed"></div>
    <div class="cta-band">Call or email to request complementary planning session</div>
    <div class="name-band">
      <p class="advisor">Reed Halloway III, RAS, CPSA, CWTA</p>
      <p class="role">Title: Managing Principal and Sr. Financial Advisor</p>
    </div>
  </section>

  <section class="postcard back">
    <svg class="shapes" width="560" height="400" viewBox="0 0 560 400">
      <defs>
        <linearGradient id="penPhoto" x1="0" y1="0" x2="1" y2="1">
          <stop offset="0" stop-color="#1f78c4"/><stop offset=".55" stop-color="#1660b4"/><stop offset="1" stop-color="#0c3d8c"/>
        </linearGradient>
      </defs>
      <path d="M0 0 H230 Q360 190 300 400 H0 Z" fill="url(#penPhoto)" role="img" aria-label="Blue-toned photo of a pen reviewing a financial chart"/>
    </svg>
    <div class="fiduciary">
      <h3>Fiduciary Standards</h3>
      <ol>
        <li>Put the client's best interests first;</li>
        <li>Act with prudence: reasonable care, diligence, and professional judgment;</li>
        <li>Provide full disclosure of all important facts;</li>
        <li>Avoid conflicts of interest; disclose conflicts to clients and fairly manage, in the client's favor, any unavoidable conflicts.</li>
      </ol>
    </div>
    <p class="slogan">“Adding someone with HEIGHT to your personal team of professionals”</p>
    <ul class="height-list">
      <li>H: Honest</li>
      <li>E: Experienced &amp; Educated</li>
      <li>I: Integrity</li>
      <li>G: a belief in “giving first”</li>
      <li>H: Hardworking</li>
      <li>T: Trustworthy</li>
    </ul>
    <address class="return-address">
      <span class="brand-name"><i></i>The Wexmoor Group, LLC</span>
      480 Harlan Street NW<br>Suite 310<br>Washington, DC 20010<br>Phone (555) 014-2287<br>Email: rhalloway@wexmoorgroup.example<br>www.wexmoorgroupdc.example
    </address>
    <div class="stamp-box" aria-label="ADPS postage area"></div>
    <div class="address-lines"><span></span><span></span><span></span><span></span></div>
  </section>

</main>
</body>
</html>
```